A colourful crystal mystical tapestry

I need an image for my book cover. The title of the book is A Harbour of Lanterns . Below, the subtitle is Along the Copper Road. The crystals move from bottom right to one third up the cover and into the middle. Stop below book title. (Book is 9x6). The crystals have to look like a multi-colour tapestry. Real crystals appear like they are gently exploding from the bottom right of the cover. More like movement than rocketships pls. But not a bunch of fragments. More clustered together. The upper cover will be white. They crystals are multi-covered bright - shinning. It can not be a bad AI image. It must be sharp and brilliant - a tapestry of colours. It is a spiritual book so, it needs to feel as such. If another creative idea comes to mind...give it a try.. I am open to something completely different as long as if is a multi-colour adult appealing spiritual unique image- which represents the title well. THANKS in advance.

Target Market(s)

Readers of multi-dimensional stories. ADULTS

Industry/Entity Type

Spirituality. Beautiful interesting intriguing.

Requirements
Nice to have
• It's tapestry, not chaos per say.
Should not have
• Anything crappy space like AI I can easily create. Be unique.

```html
<!DOCTYPE html>
<html lang="en">
<head>
<meta charset="UTF-8">
<title>A Harbour of Lanterns: Book Cover</title>
<link rel="stylesheet" href="https://fonts.googleapis.com/css2?family=Cinzel:wght@600;700&family=Montserrat:wght@400&display=swap">
<style>
  :root {
    --stage: #000000;
    --paper: #ffffff;
    --paper-cool: #eef3fb;
    --ink-navy: #213a6c;
    --gold: #f0a81c;
    --crystal-blue: #3f6fc4;
    --crystal-violet: #8a4fb8;
    --crystal-pink: #e06aa6;
    --crystal-flame: #ffb21e;
  }
  * { margin: 0; padding: 0; box-sizing: border-box; }
  html, body {
    width: 1200px;
    height: 1200px;
    overflow: hidden;
    background: var(--stage);
  }
  .cover {
    position: absolute;
    left: 250px;
    top: 75px;
    width: 700px;
    height: 1050px;
    background: linear-gradient(180deg, var(--paper) 0%, var(--paper) 70%, var(--paper-cool) 100%);
    overflow: hidden;
  }
  .title {
    position: absolute;
    left: 0;
    width: 100%;
    text-align: center;
    font-family: "Cinzel", "Trajan Pro", serif;
    font-weight: 700;
    color: var(--ink-navy);
    line-height: 1;
  }
  .title-line-1 { top: 62px; font-size: 74px; letter-spacing: 0.01em; }
  .title-line-2 { top: 150px; font-size: 104px; letter-spacing: 0.01em; }
  .subtitle {
    position: absolute;
    top: 318px;
    left: 0;
    width: 100%;
    text-align: center;
    font-family: "Montserrat", "Helvetica Neue", sans-serif;
    font-weight: 400;
    font-size: 38px;
    letter-spacing: 0.07em;
    color: var(--gold);
    text-transform: uppercase;
  }
  .crystal-art {
    position: absolute;
    left: 30px;
    top: 310px;
    width: 670px;
    height: 630px;
  }
  .author {
    position: absolute;
    top: 963px;
    left: 0;
    width: 100%;
    text-align: center;
    font-family: "Cinzel", "Trajan Pro", serif;
    font-weight: 700;
    font-size: 60px;
    letter-spacing: 0.02em;
    color: var(--ink-navy);
    line-height: 1;
  }
</style>
</head>
<body>
  <main class="cover">
    <h1>
      <span class="title title-line-1">A HARBOUR OF</span>
      <span class="title title-line-2">LANTERNS</span>
    </h1>
    <p class="subtitle">Along the Copper Road</p>

    <svg class="crystal-art" viewBox="0 0 670 630" role="img" aria-label="Illustration of a cluster of multicoloured blue, violet and pink crystals bursting outward from a glowing golden centre">
      <defs>
        <radialGradient id="burst" cx="52%" cy="60%" r="50%">
          <stop offset="0%" stop-color="var(--crystal-flame)" />
          <stop offset="22%" stop-color="#f36a3a" />
          <stop offset="45%" stop-color="var(--crystal-violet)" />
          <stop offset="70%" stop-color="var(--crystal-blue)" stop-opacity="0.75" />
          <stop offset="100%" stop-color="var(--crystal-pink)" stop-opacity="0" />
        </radialGradient>
      </defs>
      <rect width="670" height="630" fill="url(#burst)" />
    </svg>

    <p class="author">RUTH CALLOWAY</p>
  </main>
</body>
</html>
```